High Quality Business card for Property Management Agency - Super Classy and professional design

High Quality Business card design.

We need a business card designed for our Property Management Agency.
We are located on Sydney's Northern Beaches and manage beautiful properties along the beach and harbor.
We need a design that oozes modern, classy and professional.
I would like it to be double sided with contact details and logo on the front and just the logo on the back.

I need a print ready PDF version of the file as well as an editable photoshop (PSD) version of the file.

Logo and information details attached.

Target Market(s)

Property owners/investors, Male and Female Aged 28-65

Industry/Entity Type

Real Estate

Contact Information for Business Card

Tom Carrick
Tel: 0467 239 018
Email: tom@harvestlaneestates.com.au
Website: www.harvestlaneestates.com.au
Address: Level 2, 17 Wattlecourt Rd, Dunmarra NSW 2187

Font styles to use
Sans Serif

Requirements
Must have
• - Logo front and back
• - Business card details listed above and attached
• - Colour
Nice to have
• Sleek and professional

```html
<!DOCTYPE html>
<html lang="en">
<head>
<meta charset="utf-8">
<title>Harvest Lane Estates – Business Cards</title>
<link href="https://fonts.googleapis.com/css2?family=Arimo:wght@400;700&display=swap" rel="stylesheet">
<style>
  :root {
    --bg: #e6e7e8;
    --card: #ffffff;
    --ink: #222628;
    --grey: #6f7376;
    --teal: #3aa3ad;
  }
  * { margin: 0; padding: 0; box-sizing: border-box; }
  html, body { width: 1200px; height: 900px; overflow: hidden; }
  body {
    background: var(--bg);
    font-family: "Arimo", Arial, sans-serif;
    position: relative;
  }
  .card {
    position: absolute;
    width: 700px;
    height: 400px;
    background: var(--card);
    box-shadow: 0 6px 18px rgba(0,0,0,0.12);
    overflow: hidden;
  }
  .card--back { left: 150px; top: 30px; }
  .card--front { left: 350px; top: 470px; }

  .accent-line {
    position: absolute;
    height: 2px;
    background: var(--teal);
    right: 0;
  }
  .card--back .accent-line { left: 360px; top: 332px; }
  .card--front .accent-line { left: 300px; top: 372px; }

  .brand {
    position: absolute;
    display: flex;
    align-items: center;
    gap: 12px;
    color: var(--ink);
    font-weight: 700;
    text-transform: uppercase;
    letter-spacing: 0.5px;
    white-space: nowrap;
  }
  .brand__mark {
    width: 14px; height: 14px;
    background: var(--teal);
    border-radius: 50%;
    flex: none;
  }
  .card--back .brand { left: 150px; top: 178px; font-size: 34px; }
  .card--front .brand { right: 44px; top: 90px; font-size: 26px; }

  .contact {
    position: absolute;
    left: 48px;
    top: 180px;
    color: var(--grey);
    font-size: 17px;
    line-height: 1.3;
  }
  .contact__name {
    color: var(--teal);
    font-weight: 700;
    font-size: 24px;
    text-transform: uppercase;
    letter-spacing: 0.5px;
    margin-bottom: 10px;
  }
  .contact__address { margin-bottom: 10px; }
  .contact__list { list-style: none; }
  .contact__item {
    display: flex;
    align-items: center;
    gap: 10px;
    margin-bottom: 3px;
    white-space: nowrap;
  }
  .contact__item--phone { color: var(--ink); font-weight: 700; opacity: 0.8; }
  .icon { width: 16px; height: 16px; flex: none; }
</style>
</head>
<body>

<section class="card card--back" aria-label="Card back">
  <div class="brand"><span class="brand__mark"></span>Harvest Lane Estates</div>
  <div class="accent-line"></div>
</section>

<section class="card card--front" aria-label="Card front">
  <div class="brand"><span class="brand__mark"></span>Harvest Lane Estates</div>

  <div class="contact">
    <p class="contact__name">Tom Carrick</p>
    <p class="contact__address">Level 2, 17 Wattlecourt Rd<br>Dunmarra NSW 2187</p>
    <ul class="contact__list">
      <li class="contact__item contact__item--phone">
        <svg class="icon" viewBox="0 0 16 16" aria-hidden="true">
          <circle cx="8" cy="8" r="8" fill="#3aa3ad"/>
          <path d="M5.2 4.2l1.5-.3.8 2-1 .8c.5 1.1 1.3 1.9 2.4 2.4l.8-1 2 .8-.3 1.5c-3.6.2-6.4-2.6-6.2-6.2z" fill="#fff"/>
        </svg>
        0467 239 018
      </li>
      <li class="contact__item">
        <svg class="icon" viewBox="0 0 16 16" aria-hidden="true">
          <circle cx="8" cy="8" r="8" fill="#3aa3ad"/>
          <rect x="4" y="5" width="8" height="6" fill="#fff"/>
          <path d="M4 5l4 3.2L12 5" fill="none" stroke="#3aa3ad" stroke-width="1"/>
        </svg>
        tom@harvestlaneestates.com.au
      </li>
      <li class="contact__item">
        <svg class="icon" viewBox="0 0 16 16" aria-hidden="true">
          <circle cx="8" cy="8" r="8" fill="#3aa3ad"/>
          <circle cx="8" cy="8" r="4" fill="none" stroke="#fff" stroke-width="1.1"/>
          <path d="M4 8h8M8 4c-1.6 2.4-1.6 5.6 0 8M8 4c1.6 2.4 1.6 5.6 0 8" fill="none" stroke="#fff" stroke-width="0.9"/>
        </svg>
        www.harvestlaneestates.com.au
      </li>
    </ul>
  </div>

  <div class="accent-line"></div>
</section>

</body>
</html>
```